Onboarding project UI redesign

The web site is used to onboard clients via a video-identification process.
The end-user first tests his computer, then enters his order details and waits for an operator engagement.
When the operator engages the customer, they go through some identification steps together, ending on a contract signature page.

Target Market(s)

Finance B2C

Industry/Entity Type

Finance

Coding

Coded - Design and coding required

Number of Pages Required

5+ page

Font styles to use
Sans Serif

Requirements
Must have
• Professional UI
• Design for mobile devices

```html
<!DOCTYPE html>
<html lang="en">
<head>
<meta charset="utf-8">
<title>Novera Bank – Video Identification</title>
<link href="https://fonts.googleapis.com/css2?family=Titillium+Web:wght@400;600;700&display=swap" rel="stylesheet">
<style>
:root{
  --blue:#0a84f5;
  --blue-soft:#3ea0f0;
  --navy:#1d4d8c;
  --ink:#1c1c1c;
  --muted:#555;
  --label:#4a4a4a;
  --panel-bg:#e6e6e6;
  --white:#fff;
  --card:#f3f4f6;
  --dark-tab:#1b2736;
  --title-bar:#454545;
  --red:#e8474c;
}
*{box-sizing:border-box;margin:0;padding:0}
html,body{width:1200px;height:823px;overflow:hidden;background:var(--white);font-family:"Titillium Web",sans-serif;color:var(--ink)}
.app{position:relative;width:1200px;height:823px}
.header{position:absolute;left:0;top:0;width:1200px;height:88px;background:var(--white);display:flex;justify-content:center;align-items:center}
.brand{display:flex;align-items:center;gap:10px;font-size:30px;font-weight:600;color:var(--navy);letter-spacing:1px}
.brand-mark{width:18px;height:18px;background:var(--navy)}
.sidebar{position:absolute;left:0;top:88px;width:77px;height:735px;background:var(--white)}
.nav-item{position:absolute;left:0;width:77px;display:flex;flex-direction:column;align-items:center;font-size:8px;font-weight:700;color:#222;text-transform:uppercase}
.nav-item svg{margin-bottom:4px}
.nav-item.active{top:0;height:75px;background:var(--blue);color:var(--white);justify-content:center}
.stage{position:absolute;left:77px;top:88px;width:1123px;height:735px;background:var(--panel-bg)}
.video{position:absolute;left:1px;top:1px;width:777px;height:486px;background:radial-gradient(ellipse at 50% 60%,#8d8f93 0%,#c9cbcf 45%,#ececee 80%);border:1px solid #cfcfcf}
.controls{position:absolute;left:28px;bottom:24px;display:flex;gap:8px}
.ctrl{width:34px;height:34px;border-radius:50%;background:var(--white);display:flex;align-items:center;justify-content:center}
.ctrl.hangup{background:var(--red)}
.submit{position:absolute;right:27px;bottom:25px;width:131px;height:35px;border-radius:18px;background:var(--white);display:flex;align-items:center;padding-left:28px;font-size:17px;color:#333;letter-spacing:.5px}
.submit .plus{position:absolute;right:5px;top:5px;width:25px;height:25px;border-radius:50%;background:var(--blue-soft);color:var(--white);font-size:18px;line-height:24px;text-align:center}
.tabs{position:absolute;left:488px;top:517px;display:flex;gap:5px}
.tab{height:27px;border-radius:14px;background:#eeeeee;font-size:14px;font-weight:600;color:#333;display:flex;align-items:center;justify-content:center}
.tab.active{background:var(--dark-tab);color:var(--white)}
.steps{position:absolute;left:22px;top:575px;display:flex}
.step{position:relative;width:154px;height:128px;border-radius:12px;background:var(--card);border:2px solid var(--blue);padding:18px 12px 0;margin-right:25px}
.step.current{border:none;width:152px;box-shadow:0 2px 8px rgba(0,0,0,.2);padding:20px 12px 0}
.step .num{font-size:10px;font-weight:600;color:#333}
.step .num b{font-size:18px;font-weight:600}
.step .label{margin-top:14px;font-size:12.5px;font-weight:600;color:#444;line-height:16px;text-transform:uppercase}
.step .tick{position:absolute;right:10px;top:8px}
.aside-step{position:absolute;left:904px;top:108px;color:var(--blue);font-size:22px;font-weight:600}
.aside-step b{font-size:40px;font-weight:700}
.data-card{position:absolute;left:887px;top:167px;width:274px;height:610px;background:var(--white);border-radius:14px;padding:17px 17px 0}
.data-title{height:37px;background:var(--title-bar);color:var(--white);font-size:18px;font-weight:600;padding-left:12px;line-height:37px}
.intro{margin-top:17px;width:236px;font-size:16.5px;line-height:20px;color:var(--muted)}
.fields{margin-top:9px}
.field{margin-top:9px}
.field dt{font-size:14.5px;line-height:20px;font-weight:600;color:var(--label)}
.field dd{margin-top:7px;font-size:19.5px;line-height:24px;color:#111}
.confirm{position:absolute;left:63px;top:556px;width:120px;height:25px;border-radius:13px;background:var(--blue);color:var(--white);font-size:16px;font-weight:600;text-align:center;line-height:25px}
</style>
</head>
<body>
<div class="app">
  <header class="header">
    <div class="brand"><span class="brand-mark"></span>NOVERA BANK</div>
  </header>

  <nav class="sidebar">
    <div class="nav-item active">
      <svg width="22" height="20" viewBox="0 0 22 20"><rect x="1" y="5" width="20" height="14" rx="2" fill="#fff"/><rect x="7" y="1" width="8" height="5" rx="1" fill="none" stroke="#fff" stroke-width="2"/></svg>
      Check in
    </div>
    <div class="nav-item" style="top:95px">
      <svg width="22" height="16" viewBox="0 0 22 16"><rect x="0" y="1" width="15" height="14" rx="2" fill="#111"/><path d="M15 6l7-4v12l-7-4z" fill="#111"/></svg>
      Record
    </div>
    <div class="nav-item" style="top:160px">
      <svg width="22" height="24" viewBox="0 0 22 24"><rect x="2" y="3" width="15" height="20" fill="#fff" stroke="#111" stroke-width="1.5"/><path d="M5 10h9M5 14h9M5 18h9" stroke="#111"/><circle cx="17" cy="5" r="5" fill="#111"/><path d="M14.5 5l2 2 3-3.5" stroke="#fff" stroke-width="1.3" fill="none"/></svg>
      Profile
    </div>
    <div class="nav-item" style="top:226px">
      <svg width="22" height="18" viewBox="0 0 22 18"><path d="M1 1h16v10H6l-4 4v-4H1z" fill="#111"/><path d="M19 6h2v10l-3-3h-8v-1" fill="none" stroke="#111"/></svg>
      SMS
    </div>
    <div class="nav-item" style="top:297px">
      <svg width="22" height="18" viewBox="0 0 22 18"><rect x="1" y="3" width="20" height="14" rx="1" fill="#111"/><rect x="8" y="0" width="6" height="5" fill="#fff" stroke="#111"/><circle cx="7" cy="9" r="2.5" fill="#fff"/><path d="M3 15c0-3 8-3 8 0z" fill="#fff"/><path d="M13 9h6M13 12h6" stroke="#fff"/></svg>
      ID document
    </div>
    <div class="nav-item" style="top:366px">
      <svg width="24" height="16" viewBox="0 0 24 16"><path d="M1 6l6-4 5 3 5-3 6 4-4 4-6 5-4-3-4-1z" fill="#111"/><path d="M9 7l3 2 3-2" stroke="#fff" fill="none"/></svg>
      Contract
    </div>
  </nav>

  <main class="stage">
    <section class="video" role="img" aria-label="Live video feed of the customer during identification">
      <div class="controls">
        <span class="ctrl"><svg width="16" height="12" viewBox="0 0 16 12"><rect x="0" y="1" width="11" height="10" rx="1" fill="#111"/><path d="M11 4.5l5-3v9l-5-3z" fill="#111"/></svg></span>
        <span class="ctrl"><svg width="11" height="11"><rect width="11" height="11" fill="#111"/></svg></span>
        <span class="ctrl hangup"><svg width="14" height="14" viewBox="0 0 14 14"><path d="M3 1l2 3-1.5 1.5c.8 2 2.5 3.7 4.5 4.5L9.5 8.5l3 2-1 2.5C6 13 1 8 1 2.5z" fill="#fff"/></svg></span>
      </div>
      <div class="submit">SUBMIT<span class="plus">+</span></div>
    </section>

    <div class="tabs">
      <span class="tab active" style="width:99px">QUALITY</span>
      <span class="tab" style="width:72px">VIDEO</span>
      <span class="tab" style="width:72px;margin-left:7px">AUDIO</span>
    </div>

    <div class="steps">
      <div class="step">
        <svg class="tick" width="17" height="17" viewBox="0 0 17 17"><circle cx="8.5" cy="8.5" r="7.5" fill="none" stroke="#0a84f5" stroke-width="1.3"/><path d="M5 8.8l2.5 2.4L12 6" fill="none" stroke="#0a84f5" stroke-width="1.3"/></svg>
        <div class="num">STEP <b>1/11</b></div>
        <div class="label">Confirm quality of connection</div>
      </div>
      <div class="step">
        <svg class="tick" width="17" height="17" viewBox="0 0 17 17"><circle cx="8.5" cy="8.5" r="7.5" fill="none" stroke="#0a84f5" stroke-width="1.3"/><path d="M5 8.8l2.5 2.4L12 6" fill="none" stroke="#0a84f5" stroke-width="1.3"/></svg>
        <div class="num">STEP <b>2/11</b></div>
        <div class="label">Recording confirmation</div>
      </div>
      <div class="step current">
        <div class="num">STEP <b>3/11</b></div>
        <div class="label">Confirm personal data</div>
      </div>
    </div>
  </main>

  <div class="aside-step">STEP <b>3/11</b></div>

  <aside class="data-card">
    <div class="data-title">CONFIRM PERSONAL DATA</div>
    <p class="intro">Now we will verify your data together. If everything is correct, please press the CONFIRM button.</p>
    <dl class="fields">
      <div class="field"><dt>SIMCARD ID</dt><dd>040517283946102375</dd></div>
      <div class="field"><dt>Name and Surname</dt><dd>Demo Customer</dd></div>
      <div class="field"><dt>Date of Birth</dt><dd>01/01/1980</dd></div>
      <div class="field"><dt>Place of Birth</dt><dd>Borgo Castellino</dd></div>
      <div class="field"><dt>National Insurance number</dt><dd>TSTCM80A01B772Q</dd></div>
      <div class="field"><dt>ID Document Type</dt><dd>1</dd></div>
    </dl>
    <div class="confirm">CONFIRM</div>
  </aside>
</div>
</body>
</html>
```